Website for AV installation with booking system and e-commerce

Company: Velqora
Tag Line: Audio Visual and Security System Installations
We need a website for an AV company based in Sydney Australia. We specialise in Audio Visual, CCTV (security cameras), and Data Cabling.
The purpose of the website is that customers book their installation online with a live booking system.
We are looking for the following:
- Creative and modern design
- easy to use - keep in mind that the user who will book will have little knowledge in technology.
- clean and organised
- colours to work in well with our logo we also like royal to navy blue, but we are open to other suggested what works well with our logo.
We want customers to be able to add products needed for their installation ie when booking to wall mount their TV they can choose to add a TV bracket and cables to the cart and vise-versa buy a bracket or cables and add to cart the installation.
Tabs to be included:
About us
Gallery
Contact Us
Home
Services (there are three services that we offer - Residential, Corporate and Retail)
Products
Book Online/Cart (checkout)
Temporary website checkout: www.velqora.com.au, please note this is very basic and we do not want a copy of this. This is purely to give you an idea of our company.
Good Luck!
Updates
Target Market(s)
home owners/renters, business owners, archiects/designers, builders
Industry/Entity Type
E-Commerce
Look and feel

```html
<!DOCTYPE html>
<html lang="en">
<head>
<meta charset="utf-8">
<title>Velqora – Audio Visual and Security System Installations</title>
<link rel="stylesheet" href="https://fonts.googleapis.com/css2?family=PT+Sans:wght@400;700&family=Noto+Sans:wght@400&display=swap">
<style>
:root{
  --navy-deep:#0f1c2e;
  --navy:#1d3250;
  --navy-light:#2a4466;
  --accent:#e0161b;
  --text:#4a4a4a;
  --muted:#8a8a8a;
  --white:#ffffff;
  --strip-top:#f7f7f7;
  --strip-bottom:#e6e6e6;
  --btn-top:#6f7680;
  --btn-bottom:#3c424b;
  --icon:#5d6470;
}
*{margin:0;padding:0;box-sizing:border-box}
html,body{width:1118px;height:1200px;overflow:hidden;background:var(--white)}
body{position:relative;font-family:"Noto Sans",Verdana,sans-serif;color:var(--text)}
.abs{position:absolute}

/* header */
.site-header{left:0;top:0;width:1118px;height:94px;
  background:radial-gradient(ellipse at 50% 0%,var(--navy-light),var(--navy) 45%,var(--navy-deep));
  border-bottom:3px solid #3a4a5e}
.brand{left:122px;top:28px;display:flex;align-items:center;gap:10px;
  font-family:"PT Sans",sans-serif;font-weight:700;font-size:34px;color:var(--white);letter-spacing:1px}
.brand-dot{width:16px;height:16px;border-radius:50%;background:var(--accent)}
.main-nav{position:absolute;right:118px;top:28px;display:flex;align-items:center;gap:19px}
.main-nav a{display:flex;align-items:center;gap:6px;height:38px;font-family:"PT Sans",sans-serif;font-size:12.5px;letter-spacing:1.8px;
  color:#e3e8ef;text-decoration:none;text-transform:uppercase;white-space:nowrap}
.main-nav .active{width:76px;justify-content:center;color:var(--accent);
  background:linear-gradient(#1c2a3e,#111c2b);border:1px solid #3d4d63;box-shadow:0 0 4px rgba(0,0,0,.6)}

/* hero */
.hero-photo{left:0;top:94px;width:1118px;height:346px;
  background:linear-gradient(180deg,#4f7680 0%,#6a8f98 45%,#c5d6da 72%,#e9eff0 100%)}
.hero-card{left:728px;top:123px;width:264px;height:276px;background:rgba(70,74,80,.82);padding:17px 20px}
.hero-card h1{font-family:"PT Sans",sans-serif;font-weight:700;font-size:21.5px;line-height:27px;color:var(--white);text-transform:uppercase}
.hero-card p{margin-top:10px;font-size:9.8px;line-height:20px;color:#eceff2}
.btn{display:block;text-align:center;color:var(--white);text-decoration:none;font-family:"PT Sans",sans-serif;
  background:linear-gradient(var(--btn-top),var(--btn-bottom));border:1px solid #1c1f24;border-radius:2px;
  box-shadow:inset 0 1px 0 rgba(255,255,255,.25)}
.hero-card .btn{position:absolute;left:75px;top:223px;width:114px;height:35px;line-height:33px;font-size:13px}

/* info strip */
.info-strip{left:0;top:440px;width:1118px;height:82px;background:linear-gradient(var(--strip-top),var(--strip-bottom));
  border-bottom:1px solid #cfcfcf;box-shadow:0 3px 4px rgba(0,0,0,.05)}
.info-item{position:absolute;top:28px;font-size:12.5px;line-height:17px;letter-spacing:.4px;color:#333}
.info-item span{display:block;color:var(--muted)}
.info-item.current{color:var(--accent)}
.info-divider{position:absolute;top:8px;width:1px;height:70px;background:#d8d8d8;box-shadow:1px 0 0 #fff}

/* content */
.round-icon{width:33px;height:33px;border-radius:50%;background:radial-gradient(circle at 40% 30%,#8a909a,var(--icon));
  display:flex;align-items:center;justify-content:center;box-shadow:0 1px 2px rgba(0,0,0,.3)}
.section-title{font-family:"PT Sans",sans-serif;font-weight:400;font-size:17.5px;letter-spacing:2.2px;color:#3b3b3b;text-transform:uppercase}
.body-copy{font-size:11.3px;line-height:22px;letter-spacing:.75px;color:var(--text)}
.body-copy em{font-style:normal;color:var(--accent)}
.read-link{color:var(--accent);font-size:11.3px;letter-spacing:.8px;text-decoration:none}
.col-divider{left:705px;top:563px;height:129px;border-left:1px dotted #b9b9b9}
.rule{left:120px;top:823px;width:874px;border-top:2px dotted #cfcfcf}
.product{width:162px;height:161px;background:var(--white);border:1px solid #e3e3e3;box-shadow:0 1px 2px rgba(0,0,0,.06);padding:7px}
.product-photo{width:100%;height:100%}
.more-btn{left:119px;top:1020px;width:115px;height:36px;line-height:34px;font-size:12.5px;font-weight:700}

/* footer */
.site-footer{left:0;top:1096px;width:1118px;height:104px;
  background:radial-gradient(ellipse at 50% 100%,var(--navy-light),var(--navy) 50%,var(--navy-deep));border-top:3px solid #3a3f47}
.footer-nav{position:absolute;left:118px;top:46px;display:flex;gap:21px}
.footer-nav a{font-family:"PT Sans",sans-serif;font-size:13px;letter-spacing:.6px;color:#eef1f5;text-decoration:none}
.footer-nav .current{color:var(--accent)}
.copyright{position:absolute;right:117px;top:46px;font-family:"PT Sans",sans-serif;font-size:13px;letter-spacing:.5px;color:#eef1f5}
.copyright em{font-style:normal;color:var(--accent)}
</style>
</head>
<body>

<header class="site-header abs">
  <div class="brand abs"><span class="brand-dot"></span>Velqora</div>
  <nav class="main-nav">
    <a class="active" href="#">Home</a>
    <a href="#">About</a>
    <a href="#">Gallery</a>
    <a href="#">Services</a>
    <a href="#">Products</a>
    <a href="#">Book</a>
    <a href="#">Contact</a>
    <a href="#"><svg width="14" height="13" viewBox="0 0 14 13" fill="none" stroke="#e3e8ef" stroke-width="1.4" stroke-linejoin="round"><path d="M0 1h2.4l1.8 7.5h7.6L13.3 3H3.2"/><circle cx="5" cy="11.3" r="1" fill="#e3e8ef" stroke="none"/><circle cx="11" cy="11.3" r="1" fill="#e3e8ef" stroke="none"/></svg>Cart</a>
  </nav>
</header>

<section>
  <div class="hero-photo abs" role="img" aria-label="Living room with a cream sofa facing a wall-mounted television on a stand"></div>
  <div class="hero-card abs">
    <h1>Lorem ipsum dolor amet, consectetur adipiscing elit facre</h1>
    <p>Lorem ipsum dolor sit amet, consec tetur adipis cing elit. Aenean nisl orci condim entum ultrices co nsequat eu, vehicula act adipiscing. Aenean nisl orci condim entum ultrices co nsequat eu, vehicula act adipisci.</p>
    <a class="btn" href="#">BOOK NOW</a>
  </div>
</section>

<section class="info-strip abs">
  <div class="info-item current" style="left:117px">Picture one info<span>more text about image</span></div>
  <div class="info-divider" style="left:288px"></div>
  <div class="info-item" style="left:307px">Picture two info<span>more text about image</span></div>
  <div class="info-divider" style="left:467px"></div>
  <div class="info-item" style="left:489px">Picture three info<span>more text about image</span></div>
  <div class="info-divider" style="left:650px"></div>
  <div class="info-item" style="left:671px">Picture four info<span>more text about image</span></div>
  <div class="info-divider" style="left:832px"></div>
  <div class="info-item" style="left:853px">Picture five info<span>more text about image</span></div>
</section>

<main>
  <div class="round-icon abs" style="left:120px;top:567px">
    <svg width="18" height="16" viewBox="0 0 18 16" fill="#fff"><circle cx="11" cy="4.5" r="3.5"/><path d="M4 16c0-4 3-6.5 7-6.5s7 2.5 7 6.5z"/><circle cx="5" cy="5" r="2.6" opacity=".8"/><path d="M0 13c0-3 2-4.8 5-4.8 1 0 1.8.2 2.4.5C5 9.8 3.5 11.5 3.2 13z" opacity=".8"/></svg>
  </div>
  <h2 class="section-title abs" style="left:166px;top:574px">Lorem ispsum dolor site ametine</h2>
  <p class="body-copy abs" style="left:120px;top:609px;width:560px">Lorem ipsum dolor sit amet, consectetur adipiscing elit. <em>Nam sit amet</em> auctor quam. Nullam vulputate libero non ligula tempus at ullamcorper massa adipiscing. Proin et enim dolor. Fusce lorem ante, <em>faucibus id</em> malesuada id, bibendum ut nunc. Vivamus suscipit nunc nec urna tempus condimentum.</p>

  <div class="col-divider abs"></div>

  <div class="round-icon abs" style="left:741px;top:567px">
    <svg width="16" height="16" viewBox="0 0 16 16" fill="none" stroke="#fff" stroke-width="2" stroke-linecap="round"><path d="M7 9l2-2"/><path d="M6 7.5 4 9.5a2.5 2.5 0 0 0 3.5 3.5l2-2"/><path d="M10 8.5l2-2A2.5 2.5 0 0 0 8.5 3l-2 2"/></svg>
  </div>
  <h2 class="section-title abs" style="left:786px;top:574px">Ispsumel&nbsp; sirote</h2>
  <p class="body-copy abs" style="left:743px;top:609px;width:262px">Lorem ipsum dolor sit amet, consectetur adipiscing elit. Nam sit amet auctor quam. Nullam vulputate libero non ligula tempus at ullamcorper elluni tyureging sertinuy olo inyterus polline redewext inne.</p>
  <a class="read-link abs" style="left:743px;top:732px" href="#">read more &gt;</a>

  <div class="round-icon abs" style="left:120px;top:747px">
    <svg width="18" height="18" viewBox="0 0 18 18" fill="#fff"><path d="M7.6 1h2.8l.4 2.2 1.5.7 1.9-1.3 2 2-1.3 1.9.7 1.5 2.2.4v2.8l-2.2.4-.7 1.5 1.3 1.9-2 2-1.9-1.3-1.5.7-.4 2.2H7.6l-.4-2.2-1.5-.7-1.9 1.3-2-2 1.3-1.9-.7-1.5L0 10.4V7.6l2.2-.4.7-1.5L1.6 3.8l2-2 1.9 1.3 1.5-.7z"/><circle cx="9" cy="9" r="3" fill="#6a707a"/></svg>
  </div>
  <h2 class="section-title abs" style="left:165px;top:754px">Latest products</h2>
  <p class="body-copy abs" style="left:120px;top:791px">vulputate libero non ligula tempus at ullamcorper massa adipiscing malesuada id, bibendum ut nunc.</p>
  <div class="rule abs"></div>

  <div class="product abs" style="left:118px;top:837px"><div class="product-photo" role="img" aria-label="Wall-mounted television above a white media unit" style="background:linear-gradient(#2b3a48 0%,#34424f 50%,#e8e8e8 62%,#f2f2f2 82%,#c8b89a 100%)"></div></div>
  <div class="product abs" style="left:294px;top:837px"><div class="product-photo" role="img" aria-label="Television on a swivel bracket in a kitchen" style="background:linear-gradient(#e6e2da 0%,#d4d0c8 55%,#bdb7ad 80%,#8a6a4a 100%)"></div></div>
  <div class="product abs" style="left:476px;top:837px"><div class="product-photo" role="img" aria-label="Security camera monitor installed in a shop" style="background:linear-gradient(135deg,#4a4742 0%,#6b665f 45%,#d9d5cc 75%,#c4bfb5 100%)"></div></div>
  <div class="product abs" style="left:657px;top:837px"><div class="product-photo" role="img" aria-label="Boardroom display on a wall above a meeting table" style="background:linear-gradient(#c9cdd2 0%,#b9bfc7 55%,#9a6a3a 78%,#2a2f3a 100%)"></div></div>
  <div class="product abs" style="left:839px;top:837px"><div class="product-photo" role="img" aria-label="Television mounted above a fireplace and console" style="background:linear-gradient(#ecebe6 0%,#dedcd4 55%,#f4f3ef 75%,#6a4a32 100%)"></div></div>

  <a class="btn more-btn abs" href="#">Read more</a>
</main>

<footer class="site-footer abs">
  <nav class="footer-nav">
    <a class="current" href="#">home</a>
    <a href="#">about</a>
    <a href="#">services</a>
    <a href="#">gallery</a>
    <a href="#">products</a>
    <a href="#">book</a>
    <a href="#">contact</a>
    <a href="#">cart</a>
  </nav>
  <p class="copyright">Copyright <em>2013</em> &nbsp; | &nbsp; All rights resvered</p>
</footer>

</body>
</html>
```